hotel renovation business brochure 1 page front and back

Our current brochure is dated. It has too much information hence the key messages are getting lost. Key messages: one stop shopping or turn key services for hotel renovations; cheaper and quicker to renovate. The only art work that cant be changes is the logo. Using the material in the brochure, create a more concise message to clients while still informing them of all the services we do. Need to update color scheme to match the logo. Would like to have a few examples of renovation we have done and possibly a listing of hotel brands we have worked on.

Target Market(s)

Hotel management companies, hotel investment companies, hotel owners

Industry/Entity Type

Hospitality

Requirements
Must have
• -1 page front and back
• -be able to communicate message as one stop shopping for hotel renovations, cheaper and faster
• - bellmoor works logo design must remain
• - consistent color palette that matches logo
• - hotel brands we have worked with
• -contact information
• -pictures of renovations. can use what is in brochure or other photos attached.
Should not have
• -too many words like in current brochure but needs to communicate our advantage and all the services we offer
• -

```html
<!DOCTYPE html>
<html lang="en">
<head>
<meta charset="utf-8">
<title>bellmoor works Raleigh – Renovation Brochure</title>
<link rel="stylesheet" href="https://fonts.googleapis.com/css2?family=Montserrat:wght@500;600;700;800&family=Open+Sans:wght@400;600&display=swap">
<style>
  :root{
    --brand-blue:#3f5f95;
    --brand-blue-dark:#2f4a78;
    --ink:#1f1f1f;
    --ink-soft:#5a5a5a;
    --paper:#ffffff;
    --backdrop:#e9e9e9;
    --tile:#f4f6fa;
    --tile-shape:#c9d3e4;
  }
  *{box-sizing:border-box;margin:0;padding:0}
  html,body{width:1200px;height:1066px;overflow:hidden}
  body{background:var(--backdrop);font-family:"Open Sans",Arial,sans-serif;color:var(--ink);position:relative}
  .sheet{position:absolute;top:196px;width:520px;height:673px;background:var(--paper);overflow:hidden;box-shadow:0 6px 22px rgba(0,0,0,.18)}
  .sheet--back{left:50px}
  .sheet--front{left:630px}
  .abs{position:absolute}
  .heading{font-family:"Montserrat",Arial,sans-serif}

  /* brand lockup */
  .brand{display:flex;align-items:center;gap:8px}
  .brand__mark{width:26px;height:26px;background:var(--brand-blue)}
  .brand__name{font-family:"Montserrat",Arial,sans-serif;font-weight:700;font-size:22px;color:var(--brand-blue);letter-spacing:-.3px}
  .brand__city{font-family:"Montserrat",Arial,sans-serif;font-weight:700;font-size:13px;letter-spacing:6px;color:var(--brand-blue);margin:4px 0 0 34px}

  /* front */
  .promise{left:240px;top:64px;width:280px;height:78px;background:var(--brand-blue);border-radius:14px 0 0 0;color:#fff;padding:14px 20px 0 26px;text-transform:uppercase;z-index:2}
  .promise__small{font-size:12px;font-weight:600;letter-spacing:.6px}
  .promise__big{font-size:19px;font-weight:700;letter-spacing:.4px;line-height:1.15}
  .hero-photo{left:22px;top:120px;width:478px;height:230px;border-radius:14px;background:linear-gradient(120deg,#d9d9d9 0%,#8d8d8d 30%,#2b2b2b 60%,#161616 100%)}
  .service-list{left:230px;top:158px;list-style:none;color:#fff;font-family:"Montserrat",Arial,sans-serif;font-size:10px;font-weight:600;letter-spacing:1.1px;line-height:18px;text-transform:uppercase}
  .gallery-band{left:0;top:318px;width:160px;height:180px;background:var(--brand-blue)}
  .gallery-photo{left:22px;width:128px;height:70px;border-radius:8px}
  .gallery-photo--lobby{top:340px;background:linear-gradient(135deg,#c98a4e,#7c4a2a 55%,#e7c79a)}
  .gallery-photo--lounge{top:418px;background:linear-gradient(135deg,#5a3a24,#b77845 50%,#d9a86c)}
  .benefits{left:190px;top:368px;width:300px;list-style:none;font-size:9.5px;color:var(--ink-soft);line-height:1.35}
  .benefits li{margin-bottom:9px}
  .benefits strong{font-family:"Montserrat",Arial,sans-serif;font-weight:700;color:var(--brand-blue);font-size:12px;text-transform:uppercase}
  .tollfree{left:26px;top:528px}
  .tollfree__label{font-family:"Montserrat",Arial,sans-serif;font-weight:700;font-size:13px;color:var(--brand-blue);letter-spacing:.4px}
  .tollfree__number{font-family:"Montserrat",Arial,sans-serif;font-weight:800;font-size:27px;color:var(--ink)}
  .address{left:230px;top:560px;font-size:12.5px;color:var(--ink-soft);line-height:1.5}
  .sheet--front .edge{left:0;bottom:0;width:100%;height:4px;background:var(--brand-blue)}

  /* back */
  .intro-note{left:290px;top:22px;width:200px;font-size:7.5px;line-height:1.35;color:var(--brand-blue)}
  .top-photo{top:78px;height:80px;border-radius:6px}
  .top-photo--bar{left:300px;width:110px;background:linear-gradient(135deg,#3a2a1e,#b88a3c 50%,#5b3f24)}
  .top-photo--room{left:416px;width:96px;background:linear-gradient(135deg,#6b4a32,#c9a57a 55%,#3d2b1e)}
  .custom-band{left:20px;top:98px;width:290px;height:84px;background:var(--brand-blue);border-radius:12px;color:#fff;padding:14px 20px}
  .custom-band__title{font-size:19px;font-weight:700;line-height:1.15;text-transform:uppercase}
  .custom-band__sub{font-size:9px;font-weight:600;letter-spacing:.6px;text-transform:uppercase;opacity:.85;margin-top:4px}
  .pillars{left:30px;top:204px;list-style:none;font-family:"Montserrat",Arial,sans-serif;font-size:10px;font-weight:600;letter-spacing:1px;color:var(--brand-blue);line-height:22px;text-transform:uppercase}
  .about{left:140px;top:204px;width:350px;font-size:9.5px;line-height:1.5;color:var(--ink-soft)}
  .contact-panel{left:0;top:330px;width:520px;height:343px;background:var(--brand-blue);color:#fff}
  .contact-panel .brand__name,.contact-panel .brand__city{color:#fff}
  .contact-panel .brand__mark{background:#fff}
  .contact-panel .brand{position:absolute;left:24px;top:30px}
  .contact-panel .brand__name{font-size:17px}
  .contact-panel .tollfree{left:24px;top:220px}
  .contact-panel .tollfree__label{color:#fff;font-size:11px}
  .contact-panel .tollfree__number{color:#fff;font-size:24px}
  .contact-panel .address{left:24px;top:282px;color:#e6ebf4;font-size:9.5px;line-height:1.45}
  .brand-grid{position:absolute;left:200px;top:22px;display:grid;grid-template-columns:repeat(4,70px);grid-auto-rows:52px;gap:8px}
  .brand-tile{background:var(--tile);display:flex;align-items:center;justify-content:center}
  .brand-tile span{display:block;background:var(--tile-shape)}
  .shape-circle{width:30px;height:30px;border-radius:50%}
  .shape-square{width:28px;height:28px}
  .shape-bar{width:46px;height:16px;border-radius:3px}
</style>
</head>
<body>

<!-- Back side -->
<section class="sheet sheet--back" aria-label="Brochure back">
  <p class="abs intro-note">Every project is led by one team from first sketch to final walkthrough, keeping budgets firm and rooms back in service sooner.</p>
  <div class="abs top-photo top-photo--bar" role="img" aria-label="Renovated hotel bar with warm lighting"></div>
  <div class="abs top-photo top-photo--room" role="img" aria-label="Renovated guest room interior"></div>
  <div class="abs custom-band heading">
    <p class="custom-band__title">100% Custom<br>and Complete!</p>
    <p class="custom-band__sub">Easy and affordable renovations</p>
  </div>
  <ul class="abs pillars">
    <li>Design</li><li>Furnish</li><li>Construct</li><li>Install</li><li>Renovate</li>
  </ul>
  <p class="abs about">bellmoor works is a full-service hotel renovation partner serving owners, investors and management groups nationwide. Our designers, buyers and builders work as one crew, so you get lower prices, tighter schedules and a finished property that meets every brand standard. Tell us your goals and we handle the rest, with one contract, one contact and one promise to deliver on time.</p>

  <div class="abs contact-panel">
    <div class="brand">
      <span class="brand__mark"></span>
      <div><span class="brand__name">bellmoor works</span></div>
    </div>
    <div class="brand-grid" aria-label="Hotel brands we have worked with">
      <div class="brand-tile"><span class="shape-square"></span></div>
      <div class="brand-tile"><span class="shape-bar"></span></div>
      <div class="brand-tile"><span class="shape-circle"></span></div>
      <div class="brand-tile"><span class="shape-square"></span></div>
      <div class="brand-tile"><span class="shape-bar"></span></div>
      <div class="brand-tile"><span class="shape-circle"></span></div>
      <div class="brand-tile"><span class="shape-bar"></span></div>
      <div class="brand-tile"><span class="shape-square"></span></div>
      <div class="brand-tile"><span class="shape-circle"></span></div>
      <div class="brand-tile"><span class="shape-bar"></span></div>
      <div class="brand-tile"><span class="shape-square"></span></div>
      <div class="brand-tile"><span class="shape-bar"></span></div>
      <div class="brand-tile"><span class="shape-bar"></span></div>
      <div class="brand-tile"><span class="shape-circle"></span></div>
      <div class="brand-tile"><span class="shape-square"></span></div>
      <div class="brand-tile"><span class="shape-bar"></span></div>
    </div>
    <div class="abs tollfree">
      <p class="tollfree__label">NATIONWIDE TOLL-FREE</p>
      <p class="tollfree__number">877-555-0142</p>
    </div>
    <p class="abs address">bellmoor works Raleigh, 2240 Linden Creek Road<br>Suite 210, Raleigh NC 27615<br>PH 919-555-0186 · FX 919-555-0187</p>
  </div>
</section>

<!-- Front side -->
<section class="sheet sheet--front" aria-label="Brochure front">
  <div class="abs" style="left:28px;top:34px">
    <div class="brand">
      <span class="brand__mark"></span>
      <span class="brand__name">bellmoor works</span>
    </div>
    <p class="brand__city">RALEIGH</p>
  </div>
  <div class="abs promise heading">
    <p class="promise__small">A complete <span class="promise__big">Renovation</span></p>
    <p class="promise__big">With just one call!</p>
  </div>
  <div class="abs hero-photo" role="img" aria-label="Renovated hotel guest room with bed and dark furnishings"></div>
  <ul class="abs service-list">
    <li>Planning</li><li>Design</li><li>Specification</li><li>FF&amp;E</li><li>Logistics</li><li>Construction</li><li>Installation</li><li>Warranty Administration</li>
  </ul>
  <div class="abs gallery-band"></div>
  <div class="abs gallery-photo gallery-photo--lobby" role="img" aria-label="Renovated hotel lobby with stone fireplace"></div>
  <div class="abs gallery-photo gallery-photo--lounge" role="img" aria-label="Renovated hotel lounge seating area"></div>
  <ul class="abs benefits">
    <li><strong>Save money.</strong> Deal with just one vendor and get huge domestic and international buying power on everything.</li>
    <li><strong>Save time.</strong> We coordinate all design, purchasing, construction and installation so your entire renovation will go faster.</li>
    <li><strong>Save stress.</strong> We manage every detail for you. There is no renovation problem we can't solve.</li>
    <li><strong>Get a better result.</strong> Your project will integrate and look better from start to finish.</li>
  </ul>
  <div class="abs tollfree">
    <p class="tollfree__label">NATIONWIDE TOLL-FREE</p>
    <p class="tollfree__number">877-555-0142</p>
  </div>
  <p class="abs address">bellmoor works Raleigh - 2240 Linden Creek Road<br>Suite 210, Raleigh NC 27615</p>
  <div class="abs edge"></div>
</section>

</body>
</html>
```